Business Card Design Project

We need a double-sided business card design for our e-commerce company. Be as creative as you can.

Reason: Change of logo

Target Market(s)

Business owners

Industry/Entity Type

E-Commerce

Requirements
Must have
• Name (editable)
Mobile number -editable
www.velbiro.com - MUST STAND OUT ALONE
Office address:
27 Marlow Street
#09-04 Westbrook Tower
Singapore 048216

```html
<!DOCTYPE html>
<html lang="en">
<head>
<meta charset="utf-8">
<title>Velbiro Business Card</title>
<link rel="stylesheet" href="https://fonts.googleapis.com/css2?family=Open+Sans:wght@400;600&display=swap">
<style>
  :root {
    --page-bg: #2a2a2a;
    --card-dark: #151515;
    --card-light: #f2f2f2;
    --brand-orange: #e2701f;
    --brand-blue: #2f7fc1;
    --label-orange: #e0531f;
    --text-light: #f4f4f4;
  }
  * { margin: 0; padding: 0; box-sizing: border-box; }
  html, body {
    width: 1200px; height: 900px; overflow: hidden;
    background: var(--page-bg);
    font-family: "Open Sans", sans-serif;
  }
  .stage {
    width: 1200px; height: 900px;
    display: flex; flex-direction: column;
    align-items: center; justify-content: center; gap: 56px;
  }
  .card {
    width: 640px; height: 366px;
    position: relative; overflow: hidden;
    background: var(--card-dark);
    box-shadow: 0 10px 30px rgba(0,0,0,.55);
  }
  /* front */
  .card--front {
    display: flex; flex-direction: column;
    align-items: center; justify-content: center;
  }
  .front-name {
    color: var(--brand-orange);
    font-weight: 600; font-size: 76px; line-height: 1;
    letter-spacing: 1px;
  }
  .front-url {
    margin-top: 14px;
    color: var(--brand-blue);
    font-size: 22px; letter-spacing: 3px;
    text-transform: uppercase;
  }
  /* back */
  .holder {
    position: absolute; left: 150px; top: 58px;
    color: var(--text-light);
  }
  .holder-name { font-size: 32px; line-height: 1.05; letter-spacing: .5px; }
  .holder-role { font-size: 22px; padding-left: 40px; line-height: 1.1; }
  .label {
    color: var(--label-orange);
    font-size: 14px; letter-spacing: .5px; text-transform: uppercase;
    margin-bottom: 8px;
  }
  .address { position: absolute; left: 400px; top: 80px; }
  .phone { position: absolute; left: 40px; top: 170px; }
  .detail {
    display: flex; gap: 10px; align-items: flex-start;
    color: var(--text-light); font-size: 14px; line-height: 1.25;
  }
  .detail svg { flex: none; margin-top: 2px; }
  .brand-band {
    position: absolute; left: 0; right: 0; bottom: 0; height: 180px;
    background: var(--card-light);
    clip-path: polygon(0 34%, 100% 0, 100% 100%, 0 100%);
  }
  .band-name {
    position: absolute; left: 40px; bottom: 18px;
    color: var(--brand-orange);
    font-weight: 600; font-size: 128px; line-height: 1;
  }
</style>
</head>
<body>
<main class="stage">
  <section class="card card--front" aria-label="Card front">
    <div class="front-name">velbiro</div>
    <div class="front-url">www.velbiro.com</div>
  </section>

  <section class="card card--back" aria-label="Card back">
    <div class="holder">
      <div class="holder-name">YOUR NAME</div>
      <div class="holder-role">Company Position</div>
    </div>

    <div class="address">
      <div class="label">Address</div>
      <div class="detail">
        <svg width="16" height="16" viewBox="0 0 16 16" aria-hidden="true">
          <path d="M8 1 L15 8 H13 V15 H3 V8 H1 Z" fill="var(--label-orange)"/>
          <rect x="6.5" y="10" width="3" height="5" fill="var(--card-dark)"/>
        </svg>
        <div>27 Marlow Street<br>#09-04 Westbrook Tower<br>Singapore 048216</div>
      </div>
    </div>

    <div class="phone">
      <div class="label">Cell Phone</div>
      <div class="detail">
        <svg width="14" height="16" viewBox="0 0 14 16" aria-hidden="true">
          <path d="M3 1 L5.5 4.5 L4 6 C5 8.5 6.5 10 8.5 11 L10 9.5 L13 12 L11 14.5 C6 14 1.5 9 1 3.5 Z" fill="var(--label-orange)"/>
        </svg>
        <div>000 000 000</div>
      </div>
    </div>

    <div class="brand-band">
      <div class="band-name">velbiro</div>
    </div>
  </section>
</main>
</body>
</html>
```